Brightmere Glowworks - Two Pages of Information and Pictures

We need a two page summary of the Service Offerings of Brightmere Glowworks - a company that installs LED Lighting. We've written the copy and picked images and chart that we like and have laid it out a word document.

We're looking for someone to design a more professional page layout than the generic Word Template. Please do not feel the current layout is suggested. It is only laid out this way because Word had that template. Be as creative as you want.

We would like the images and text to be in the same order that it is in now.

We're also in a rush so speed is appreciated. THANK YOU !!

Target Market(s)

Corporate Offices in New York

Industry/Entity Type

Lighting Fixture

Colors
85cae6
87cfc7
9bcb3c
3377b5

Requirements
Must have
• Must include two pages of the copy and images written and provided in the word document that was uploaded. Must use the Brightmere colors in the logo.
Nice to have
• An easy to read flow of images and.

```html
<!DOCTYPE html>
<html lang="en">
<head>
<meta charset="utf-8">
<title>Brightmere Glowworks – Two Page Summary</title>
<link href="https://fonts.googleapis.com/css2?family=Oswald:wght@500;600&family=Montserrat:wght@700;800&family=Open+Sans:wght@400;600;700&display=swap" rel="stylesheet">
<style>
:root{
  --blue:#1f5fb3;
  --blue-dark:#154a96;
  --blue-mid:#3377b5;
  --green:#8cc63f;
  --green-brand:#9bcb3c;
  --sky:#85cae6;
  --teal:#87cfc7;
  --grey-bg:#e4e5e7;
  --paper:#f2f2f2;
  --ink:#333;
  --title-blue:#1d55a8;
}
*{margin:0;padding:0;box-sizing:border-box}
html,body{width:1200px;height:817px;overflow:hidden;background:var(--grey-bg);font-family:"Open Sans",Arial,sans-serif;color:var(--ink)}
.canvas{position:relative;width:1200px;height:817px}
.page{position:absolute;top:68px;width:484px;height:676px;overflow:hidden;background:var(--paper);box-shadow:0 2px 8px rgba(0,0,0,.18)}
.page--front{left:93px}
.page--back{left:615px}
.abs{position:absolute}

/* shared footer */
.banner{position:absolute;left:0;top:610px;width:484px;height:38px}
.banner-text{position:absolute;left:0;top:610px;width:484px;height:34px;line-height:34px;text-align:center;font-family:"Montserrat",Arial,sans-serif;font-weight:800;font-size:18.5px;letter-spacing:2px;color:#fff}
.contact-bar{position:absolute;left:0;top:644px;width:484px;height:20px;background:var(--blue);display:flex;justify-content:space-around;align-items:center;padding:0 18px;font-size:7.6px;font-weight:600;color:#fff;letter-spacing:.2px}
.contact-bar span{display:flex;align-items:center;gap:5px}
.contact-bar svg{width:9px;height:9px}
.foot-strip{position:absolute;left:0;top:664px;width:484px;height:12px;background:var(--green)}

/* front */
.front-art{position:absolute;left:0;top:0}
.brand-name{position:absolute;left:166px;top:305px;width:160px;text-align:center;font-family:"Open Sans",Arial,sans-serif;font-weight:400;font-size:13px;letter-spacing:1px;color:#4a8f86}
.tagline{position:absolute;left:166px;top:365px;width:160px;text-align:center;font-size:8.5px;color:#444}
.headline{position:absolute;left:0;width:484px;text-align:center;font-family:"Oswald",Arial,sans-serif;font-weight:600;line-height:1;letter-spacing:-.5px}
.headline--grey{top:438px;font-size:41px;color:#e6e8ec}
.headline--green{top:480px;font-size:41px;color:var(--green)}
.front-copy{position:absolute;left:66px;top:538px;width:352px;text-align:center;font-size:7.3px;line-height:12px;color:#fff}

/* back */
.back-head{position:absolute;left:0;top:0}
.back-title{position:absolute;left:0;top:58px;width:484px;text-align:center;font-family:"Oswald",Arial,sans-serif;font-weight:600;font-size:27px;color:var(--green);letter-spacing:-.3px}
.section-title{position:absolute;left:11px;font-size:10.5px;font-weight:700;color:var(--title-blue)}
.section-title::before{content:"";position:absolute;left:-11px;top:1px;width:4px;height:11px;background:var(--blue)}
.copy{position:absolute;font-size:6.8px;line-height:10px;color:#333;text-align:justify}
.chart{position:absolute;left:253px;top:110px;width:218px;height:136px;background:#fafafa;border:1px solid #ddd}
.photo{position:absolute;left:256px;top:296px;width:216px;height:126px;background:linear-gradient(160deg,#5f7a48 0%,#7a6a52 35%,#4d6fa3 60%,#6e89b8 100%)}
.testimonial{position:absolute;left:11px;width:460px;border:1px solid #bfbfbf;text-align:center;font-size:7.4px;line-height:10.5px;color:#333;padding-top:5px}
.testimonial .who{display:block;font-weight:700;color:var(--title-blue)}
.quote-mark{position:absolute;font-family:"Oswald",Arial,sans-serif;font-weight:600;font-size:58px;line-height:1;color:#555}
</style>
</head>
<body>
<div class="canvas">

  <!-- FRONT -->
  <section class="page page--front">
    <svg class="front-art" width="484" height="470" viewBox="0 0 484 470">
      <defs>
        <linearGradient id="g-top" x1="0" y1="0" x2="1" y2="1"><stop offset="0" stop-color="#5a3d28"/><stop offset=".5" stop-color="#b08a5e"/><stop offset="1" stop-color="#e8dccb"/></linearGradient>
        <linearGradient id="g-left" x1="0" y1="0" x2="1" y2="1"><stop offset="0" stop-color="#e9ecef"/><stop offset=".6" stop-color="#a9b0b4"/><stop offset="1" stop-color="#3c4448"/></linearGradient>
        <linearGradient id="g-right" x1="0" y1="0" x2="1" y2="1"><stop offset="0" stop-color="#2a1e16"/><stop offset=".5" stop-color="#8a5a2c"/><stop offset="1" stop-color="#e0a860"/></linearGradient>
      </defs>
      <rect width="484" height="394" fill="#f4f4f4"/>
      <polygon points="0,0 140,0 0,150" fill="#8cc63f"/>
      <polygon points="0,0 95,0 0,100" fill="#79b531"/>
      <polygon points="0,0 50,0 0,52" fill="#6aa52a"/>
      <polygon points="330,0 484,0 484,170" fill="#3377b5"/>
      <polygon points="380,0 484,0 484,115" fill="#2a68ad"/>
      <polygon points="430,0 484,0 484,60" fill="#1f5fb3"/>
      <polygon points="0,280 0,380 95,380" fill="#8cc63f"/>
      <polygon points="484,240 484,380 395,380" fill="#3377b5"/>
      <polygon role="img" aria-label="Photo of a lit showroom with wood panels" points="105,0 387,0 246,175 " fill="url(#g-top)" transform="translate(0,0)"/>
      <polygon role="img" aria-label="Photo of an open-plan office under LED lighting" points="123,84 247,224 123,364 -1,224" fill="url(#g-left)"/>
      <polygon role="img" aria-label="Photo of hanging filament bulbs" points="370,100 494,240 370,380 246,240" fill="url(#g-right)"/>
      <rect y="380" width="484" height="14" fill="#8cc63f"/>
      <rect y="394" width="484" height="76" fill="#1f5fb3"/>
      <polygon points="246,208 356,320 246,432 136,320" fill="#8cc63f"/>
      <polygon points="246,213 351,320 246,427 141,320" fill="#f7f7f7"/>
    </svg>
    <div class="brand-name">BRIGHTMERE</div>
    <div class="tagline">Making LEDs beautiful.</div>

    <div class="abs" style="left:0;top:470px;width:484px;height:206px;background:var(--blue)"></div>
    <h1 class="headline headline--grey">NO UPFRONT COST</h1>
    <h2 class="headline headline--green">TURNKEY LEDS</h2>
    <p class="front-copy">Brightmere Glowworks provides LED lighting as a service – fully implemented and managed LEDs at no upfront cost. Brightmere takes the risk, hassle and capital cost out of adopting LED’s energy saving technology. Brightmere guarantees net-savings for customers on day one, and continues to guarantee savings and performance for the full term of the contract. And the savings add up! A project can be installed 2-4 weeks from kickoff, and projects continue to generate savings for up to 10 years.</p>

    <svg class="banner" viewBox="0 0 484 38"><polygon points="58,0 426,0 450,34 34,34" fill="var(--green)"/><rect y="34" width="484" height="4" fill="var(--green)"/></svg>
    <div class="banner-text">MAKING LEDS BEAUTIFUL</div>
    <div class="contact-bar">
      <span><svg viewBox="0 0 10 10"><rect x="0.5" y="2" width="9" height="6" fill="none" stroke="#fff"/><polyline points="0.5,2 5,5.5 9.5,2" fill="none" stroke="#fff"/></svg>CUSTOMERS@BRIGHTMEREGLOW.COM</span>
      <span><svg viewBox="0 0 10 10"><path d="M2 1 L4 3 L3 4.3 Q4.5 6 5.7 7 L7 6 L9 8 L7.8 9.3 Q4 8.5 0.7 2.2 Z" fill="#fff"/></svg>347 555 GLOW</span>
      <span><svg viewBox="0 0 10 10"><circle cx="5" cy="5" r="4.3" fill="none" stroke="#fff"/><ellipse cx="5" cy="5" rx="1.8" ry="4.3" fill="none" stroke="#fff"/><line x1="0.7" y1="5" x2="9.3" y2="5" stroke="#fff"/></svg>BRIGHTMEREGLOW.COM</span>
    </div>
    <div class="foot-strip"></div>
  </section>

  <!-- BACK -->
  <section class="page page--back">
    <svg class="back-head" width="484" height="100" viewBox="0 0 484 100">
      <rect width="484" height="100" fill="var(--blue)"/>
      <rect x="0" y="0" width="484" height="30" fill="#2a6cc0" opacity=".5"/>
      <polygon points="0,88 242,18 484,88 484,100 0,100" fill="#f6f6f6"/>
      <polygon points="0,88 242,18 484,88 484,91 242,22 0,91" fill="#ffffff" opacity=".7"/>
    </svg>
    <div class="back-title">BRIGHTMERE GLOWWORKS</div>

    <h3 class="section-title" style="top:106px">WHY USE BRIGHTMERE?</h3>
    <p class="copy" style="left:11px;top:124px;width:227px">Brightmere’s customers understand the value of LEDs but don’t want to deal with the risk, hassle and capital cost on their own. Brightmere starts saving customers money the first month – typically a net-savings of about 4.7 cents a square-foot per month. Brightmere will design aesthetic LED systems and install the best available technology.<br><br>Brightmere provides LEDs at the best cost with its as-a-service structure, which puts the cost of lighting into clients’ monthly operating budget for less than they save. By installing projects immediately, Brightmere eliminates the cost of foregone savings that would accumulate from delayed implementation.</p>

    <div class="chart">
      <svg width="218" height="136" viewBox="0 0 218 136">
        <text x="109" y="11" font-size="6.4" text-anchor="middle" fill="#333" font-family="Open Sans, sans-serif">Annual and Total Net-Savings of 250,000 ft2 Customer</text>
        <g stroke="#e2e2e2" stroke-width=".5">
          <line x1="30" y1="20" x2="196" y2="20"/><line x1="30" y1="40" x2="196" y2="40"/><line x1="30" y1="60" x2="196" y2="60"/><line x1="30" y1="80" x2="196" y2="80"/><line x1="30" y1="100" x2="196" y2="100"/><line x1="30" y1="120" x2="196" y2="120"/>
        </g>
        <g font-size="3.6" fill="#666" font-family="Open Sans, sans-serif">
          <text x="18" y="22">$300</text><text x="18" y="42">$250</text><text x="18" y="62">$200</text><text x="18" y="82">$150</text><text x="18" y="102">$100</text><text x="20" y="122">$50</text>
          <text x="199" y="22">$2.0</text><text x="199" y="52">$1.5</text><text x="199" y="82">$1.0</text><text x="199" y="112">$0.5</text><text x="199" y="139">$0.0</text>
        </g>
        <g fill="#87cfc7">
          <rect x="36" y="100" width="5" height="28"/><rect x="52" y="100" width="5" height="28"/><rect x="68" y="100" width="5" height="28"/><rect x="84" y="100" width="5" height="28"/><rect x="100" y="100" width="5" height="28"/>
        </g>
        <g fill="#6ab04c">
          <rect x="42" y="84" width="5" height="44"/><rect x="58" y="84" width="5" height="44"/><rect x="74" y="84" width="5" height="44"/><rect x="90" y="84" width="5" height="44"/><rect x="106" y="84" width="5" height="44"/>
          <rect x="122" y="46" width="5" height="82"/><rect x="138" y="46" width="5" height="82"/><rect x="154" y="46" width="5" height="82"/><rect x="170" y="46" width="5" height="82"/><rect x="186" y="46" width="5" height="82"/>
        </g>
        <polyline points="38,126 54,122 70,117 86,112 102,106 118,97 134,86 150,74 166,62 182,50 194,40" fill="none" stroke="#8a9aa8" stroke-width=".8"/>
        <line x1="30" y1="128" x2="196" y2="128" stroke="#999" stroke-width=".5"/>
        <g font-size="3.4" fill="#666" font-family="Open Sans, sans-serif">
          <rect x="44" y="131.5" width="6" height="1.5" fill="#87cfc7"/><text x="52" y="133.5">Annual Service</text>
          <rect x="94" y="131.5" width="6" height="1.5" fill="#6ab04c"/><text x="102" y="133.5">Annual Net-Savings</text>
          <rect x="146" y="132" width="6" height=".6" fill="#8a9aa8"/><text x="154" y="133.5">Total Net-Savings</text>
        </g>
      </svg>
    </div>

    <p class="copy" style="left:11px;top:252px;width:462px">It can be risky to adopt new technology, especially when salespeople try to sell more than is needed. Brightmere has access to better equipment and at better cost than is widely available on the open market and passes that quality and savings on to its customers. Brightmere guarantees performance for 5 years, which removes the risk of a failed project.</p>

    <h3 class="section-title" style="top:292px">THE BEST TEAM IN LEDS</h3>
    <p class="copy" style="left:11px;top:313px;width:227px">Brightmere is a team of lighting experts who get the evolution of lighting and efficiency. Simply put, we come in up every day with one goal: to provide an excellent service that saves money and uses less electricity. Part of the team focuses on the supply chain of the very best equipment that customers have come to appreciate. Part of the team focuses on the project management of each installation. And, part of the team focuses on resolving any questions customers might have in their transition. Together we make up the best team in LEDs and work tirelessly to make it easy to upgrade.</p>
    <div class="photo" role="img" aria-label="Photo of the installation team outdoors in matching blue shirts, seen from behind"></div>

    <h3 class="section-title" style="top:426px">TESTIMONIALS</h3>
    <div class="testimonial" style="top:450px;height:44px">“ Brightmere made a huge improvement in the lighting for our headquarters.<br>The installation process was as smooth as can be and the service since has been excellent.”<span class="who">HARBORLINE HEALTH</span></div>
    <div class="quote-mark" style="left:17px;top:448px">“</div>
    <div class="testimonial" style="top:502px;height:44px">“ In a museum, quality lighting is paramount. Brightmere has been a great partner in helping us transition<br>to LEDs that look great, save us money, and make lighting management so much simpler. ”<span class="who">CHILDREN’S GALLERY OF DESIGN, NEW YORK</span></div>
    <div class="testimonial" style="top:553px;height:49px">“ We are so happy to have had Brightmere’s help building out our new office space – they put their lighting expertise to work delivering beautiful LEDs and fixtures. It was cost-effective, removed lighting from the build-out budget, and it’s been a joy to work with them since.”<span class="who">CODEWRIGHT, INC</span></div>
    <div class="quote-mark" style="left:429px;top:585px">”</div>

    <svg class="banner" viewBox="0 0 484 38"><polygon points="58,0 426,0 450,34 34,34" fill="var(--green)"/><rect y="34" width="484" height="4" fill="var(--green)"/></svg>
    <div class="banner-text">MAKING LEDS BEAUTIFUL</div>
    <div class="contact-bar">
      <span><svg viewBox="0 0 10 10"><rect x="0.5" y="2" width="9" height="6" fill="none" stroke="#fff"/><polyline points="0.5,2 5,5.5 9.5,2" fill="none" stroke="#fff"/></svg>CUSTOMERS@BRIGHTMEREGLOW.COM</span>
      <span><svg viewBox="0 0 10 10"><path d="M2 1 L4 3 L3 4.3 Q4.5 6 5.7 7 L7 6 L9 8 L7.8 9.3 Q4 8.5 0.7 2.2 Z" fill="#fff"/></svg>347 555 GLOW</span>
      <span><svg viewBox="0 0 10 10"><circle cx="5" cy="5" r="4.3" fill="none" stroke="#fff"/><ellipse cx="5" cy="5" rx="1.8" ry="4.3" fill="none" stroke="#fff"/><line x1="0.7" y1="5" x2="9.3" y2="5" stroke="#fff"/></svg>BRIGHTMEREGLOW.COM</span>
    </div>
    <div class="foot-strip"></div>
  </section>

</div>
</body>
</html>
```